New Business Card Design Project

I would like my card design to look exactly like the logo, design, layout, and print of the current attached file. The only change I would like made would be for the print to say THE KMW GROUP instead of THE HALLORAN GROUP. Basically, just replace his group name with my group name. I would also like the backgroud to be the same texture and color as the attached file. I love the dark blue lettering and house logo on the card.

I am completely open to the rest of the card design. I just want something clean and simple. Only basic contact info required on the card. Maybe just name: Kyle M Warrick and cell # 555.914.2087 and email kyle@orchidhomesagent.com

```html
<!DOCTYPE html>
<html lang="en">
<head>
<meta charset="utf-8">
<title>The KMW Group — Business Card</title>
<link rel="stylesheet" href="https://fonts.googleapis.com/css2?family=Montserrat:wght@400;500&family=Roboto:wght@400&display=swap">
<style>
  :root {
    --page-bg: #e9eaec;
    --card-stock: #e6e4df;
    --card-stock-shade: #dcdad4;
    --ink-navy: #151a33;
    --card-shadow: rgba(40, 42, 50, 0.22);
  }
  * { margin: 0; padding: 0; box-sizing: border-box; }
  html, body {
    width: 1200px;
    height: 1200px;
    overflow: hidden;
    background: var(--page-bg);
  }
  .canvas {
    position: relative;
    width: 1200px;
    height: 1200px;
  }
  .card {
    position: absolute;
    left: 278px;
    width: 652px;
    height: 374px;
    background: radial-gradient(ellipse at 35% 30%, var(--card-stock) 0%, var(--card-stock-shade) 100%);
    box-shadow: 0 6px 18px var(--card-shadow);
  }
  .card--front { top: 153px; }
  .card--back { top: 663px; }

  .wordmark {
    position: absolute;
    display: flex;
    align-items: center;
    color: var(--ink-navy);
    font-family: "Montserrat", sans-serif;
    font-weight: 500;
    text-transform: uppercase;
  }
  .wordmark__square {
    background: var(--ink-navy);
    flex: none;
  }
  .wordmark__name {
    display: flex;
    flex-direction: column;
  }
  .card--front .wordmark {
    top: 30px;
    right: 60px;
    gap: 14px;
    font-size: 17px;
    letter-spacing: 2px;
    line-height: 19px;
  }
  .card--front .wordmark__square { width: 42px; height: 42px; }

  .card--back .wordmark {
    top: 50%;
    left: 50%;
    transform: translate(-50%, -50%);
    gap: 26px;
    font-size: 27px;
    letter-spacing: 3px;
    line-height: 31px;
  }
  .card--back .wordmark__square { width: 80px; height: 80px; }

  .contact {
    position: absolute;
    left: 27px;
    bottom: 16px;
    color: var(--ink-navy);
    font-family: "Roboto", sans-serif;
    font-size: 21px;
    line-height: 27px;
    list-style: none;
  }
</style>
</head>
<body>
  <main class="canvas">
    <section class="card card--front" aria-label="Card front">
      <div class="wordmark">
        <span class="wordmark__square" aria-hidden="true"></span>
        <span class="wordmark__name"><span>The</span><span>KMW</span><span>Group</span></span>
      </div>
      <ul class="contact">
        <li>Kyle M Warrick</li>
        <li>555 914 2087</li>
        <li>kyle@orchidhomesagent.com</li>
      </ul>
    </section>

    <section class="card card--back" aria-label="Card back">
      <div class="wordmark">
        <span class="wordmark__square" aria-hidden="true"></span>
        <span class="wordmark__name"><span>The</span><span>KMW</span><span>Group</span></span>
      </div>
    </section>
  </main>
</body>
</html>
```